Vacation/Holiday Home Wordpress Website

I currently have a website for our vacation/holiday rental home. It is 6 years old and needs a complete redesign to acommodate many new features available today. The existing website can be seen at www.coralwindstays.co.uk . The purpose of the website is mainly to provide useful infomation about our home, the destination of Barbados. The customer is also able to check availability and book. Please note that there is a booking element to the website which is hosted externally. This can be seen at

http://stay.reservequick-hub.net/PickArrival_Mini.asp?ref=kTR%3DWQPA%26LMN%3DHXJX

I now wish to add key functionality such as:

- Video of property and area
- Customer video testimonials
- Other useful information

The navigation, menus and buttons need to be re designed to give a modern, innovative and professional look and feel.

My customers are mainly females between the ages of 35 and 55. The website needs to reassure customers who are parting with a lot of mony by booking online. It needs to give a sense of trust as this may be a once in a lifetime trip which they have saved up for for a long time. Many visitors to the website will be referred by other websites such as www.nestroam.co.uk and www.villaquarters.co.uk.
Updates

Dear designers, 

Thank you for taking the time to write some further comments to you all. 

1. The homepage should have an availability search function as a key feature

2. The look and feel does NOT need to have the 3 feature columns like my current website has

3.  There should not be too much text on the homepage. Brief text can be included with 'more'  buttons to reveal more information 

4.  For designs that are under consideration, we will need to see a design for the other pages as they will be different to the homepage. Information from other pages on the existing website can be used. 

Reason: Dear all, I will be providing extensive feedback later today following a review that we have conducted with a group of our guests. To enable you to read and use this information, we have extended the deadline by 5 days. Thank you for the design submisions so far. We hope that the additional feedback will enable you to amend your designs appropriately. Regards Martin Elswick

Dear all,

Thank you for your designs.  I apologise that I am unable to give detailed feedback on each and every design submitted.  I will contact you individually and indicate whether we would like you to submit any further designs.  These should take into account the feedback below.

Feedback from design review group

1.  Logo should not be displayed in a white box.  It should blend in with the background or be overlayed onto the picture.

2.  There must be an availability calendar on the home page.

3.  Any background image should be subtle, maybe blurred and not distract from the main area.

4.  Text should be limited to a few key words with a 'read more' button to reveal more information.

5.  A gallery/slide show should be featured in the top part of the screen

6.  Icons can be used as navigation buttons

7.  Video testimonials is a key feature and should appear on the home page

8.   The use of bold and vibrant colours is preferred

9.   The 3 column format of the old website should not be copied

Regards

Martin

Target Market(s)

Female's, Families, 35 to 55 year olds, travellers to Barbados

Industry/Entity Type

Online

Requirements
Must have
• Pictures
Video
Testimonials
Clear and stylish navigation
Easy to use navigation
Should not have
• Dated look or feel

```html
<!DOCTYPE html>
<html lang="en">
<head>
<meta charset="utf-8">
<title>Coral Wind Stays – The Home</title>
<link href="https://fonts.googleapis.com/css2?family=Open+Sans:wght@400;600;700&display=swap" rel="stylesheet">
<style>
:root{
  --orange:#f5a623;
  --orange-dark:#e08e0b;
  --sky:#9fd3ea;
  --sand:#f1e4c6;
  --panel:#ffffff;
  --text:#4a4a4a;
  --footer:#2b2a28;
  --footer-text:#9b9890;
  --brand:#d2352e;
}
*{box-sizing:border-box;margin:0;padding:0}
html,body{width:759px;height:1200px;overflow:hidden}
body{font-family:"Open Sans",Arial,sans-serif;color:var(--text);position:relative;
  background:linear-gradient(180deg,#7fc4e6 0%,#bfe3ef 18%,#e9efe6 32%,#f4e7cc 55%,#efe0c2 100%)}
.backdrop{position:absolute;inset:0 0 74px 0;
  background:radial-gradient(ellipse at 8% 20%,rgba(60,120,70,.45),transparent 30%),
             radial-gradient(ellipse at 95% 25%,rgba(60,120,70,.35),transparent 28%)}
.site-header{position:absolute;top:0;left:0;right:0;height:96px}
.brand{position:absolute;left:72px;top:22px;display:flex;align-items:center;gap:8px;
  font-weight:700;font-size:17px;color:var(--brand);letter-spacing:.5px}
.brand-dot{width:14px;height:14px;border-radius:50%;background:var(--brand)}
.main-nav{position:absolute;right:40px;top:28px;display:flex;gap:10px;align-items:center}
.nav-pill{background:var(--orange);color:#fff;font-size:12px;font-weight:700;
  padding:7px 16px;border-radius:16px;text-transform:uppercase;border:2px solid #fff}
.social{width:28px;height:28px;border-radius:50%;background:var(--orange);border:2px solid #fff}
.panel{position:absolute;left:63px;top:96px;width:651px;height:1030px;background:var(--panel);
  border-top:4px solid var(--orange)}
.crumb{position:absolute;left:34px;top:50px;display:flex;align-items:center;gap:14px}
.pill{background:var(--orange);color:#fff;font-size:11px;font-weight:600;padding:4px 16px;border-radius:12px;text-transform:uppercase}
.pill.section{text-transform:none;font-size:13px;padding:4px 16px}
.photo{position:absolute}
.photo-hero{left:37px;top:110px;width:614px;height:298px;
  background:linear-gradient(180deg,#3f7fd0 0%,#8fbde8 35%,#e8dcc0 55%,#d9c8a0 70%,#3e7a3a 90%)}
.photo-living{left:56px;top:494px;width:241px;height:130px;
  background:linear-gradient(135deg,#e9e2d4 0%,#c9b79a 50%,#d0722a 80%,#8a5a34 100%)}
.photo-bedroom{left:56px;top:731px;width:241px;height:160px;
  background:linear-gradient(135deg,#e8e6df 0%,#c8d8dc 40%,#c9a46c 75%,#7a5a3a 100%)}
.copy{position:absolute;left:317px;width:300px;font-size:10.5px;line-height:1.5}
.copy p{margin-bottom:10px}
.copy-home{top:428px}
.bedrooms-head{position:absolute;left:317px;top:708px}
.copy-bed{top:740px}
.site-footer{position:absolute;left:0;right:0;bottom:0;height:74px;background:var(--footer);
  padding:14px 20px;font-size:9px;line-height:1.45;color:var(--footer-text)}
</style>
</head>
<body>
<div class="backdrop"></div>
<header class="site-header">
  <div class="brand"><span class="brand-dot"></span>CORAL WIND STAYS</div>
  <nav class="main-nav">
    <span class="nav-pill">The Home</span>
    <span class="nav-pill">Booking</span>
    <span class="nav-pill">Contact Us</span>
    <span class="social"></span><span class="social"></span><span class="social"></span>
  </nav>
</header>

<main class="panel">
  <div class="crumb">
    <svg width="32" height="30" viewBox="0 0 32 30" aria-hidden="true">
      <path d="M2 14 L16 2 L30 14" fill="none" stroke="#f5a623" stroke-width="3"/>
      <rect x="7" y="13" width="18" height="15" fill="none" stroke="#f5a623" stroke-width="3"/>
      <rect x="13" y="19" width="6" height="9" fill="#f5a623"/>
    </svg>
    <span class="pill">The Home</span>
  </div>

  <div class="photo photo-hero" role="img" aria-label="Exterior of the cream two-storey villa with palm trees and blue sky"></div>

  <div class="copy copy-home">
    <p>The house is air-conditioned upstairs, the spacious living area seats five in comfort.</p>
    <p>The living area boasts a full range of entertainment equipment including satellite/cable television, DVD player, CD stereo and radio. The dining area provides comfortable seating for 4 people.</p>
    <p>The kitchen is well equipped with gill, 4 ring stove, fridge, freezer, hob, oven, microwave, washing machine and clothes dryer. There is a ground floor bathroom with toilet, basin and large mirror.</p>
  </div>
  <div class="photo photo-living" role="img" aria-label="Living room with orange sofas and bright windows"></div>

  <div class="bedrooms-head"><span class="pill section">bedrooms</span></div>
  <div class="copy copy-bed">
    <p>The master bedroom is well equipped with a king sized bed, bedside tables, lamps more than ample wardrobe space. There is also a large en suite with a bath and shower. The guest bedroom has two single beds which can be joined together if required. A second bathroom is situated next to this bedroom.</p>
    <p>Both bedrooms have remote controlled air conditioning and delightful exposed beam ceilings. The second bathroom is located adjacent to the guest bedroom and includes a toilet, basin and shower.</p>
  </div>
  <div class="photo photo-bedroom" role="img" aria-label="Bright bedroom with a white bed and window view"></div>
</main>

<footer class="site-footer">
  Lorem ipsum dolor sit amet, consectetur adipiscing elit. Aliquam sed erat. Sed non ipsum. Vestibulum ante ipsum primis in faucibus orci luctus et ultrices posuere cubilia Curae. Suspendisse potenti. Nulla sagittis condimentum ligula. Suspendisse viverra placerat tortor.
</footer>
</body>
</html>
```